Marketing Agency Needs Fresh New Look

PebbleCraftHub.com is a Digital Marketing agency with locations in North Carolina and Florida. And, yes, we do custom Websites too. When we're designing for ourselves, we prefer to outsource because we typically get fresher perspectives from designers involved in the project. Which is why we're here today posting this Redesign project for our very own website.

Overall, we like our website look/feel....but don't LOVE it. We need our new site to be a bit fresher and more current using some of today's web design/development trends.

Some of the details: We want to use more current font styles and sizes (ideally, we use 3 different fonts including one "handwritten" or script font). We use the little nerdy scientist way too much throughout our website. We want to project a positive, friendly image to our customers....but we also want to be considered serious professionals in our industry(s). So, we would like to see a better mix of fun & friendly with professional & completely capable.

Here are two examples of our local competitors and websites that we think are very well done and include some of elements we're looking to see on our new site:

1) www.craftwombats.example = these guys do a great job at mixing their cartoony dinosaur with realism imagery. Very clean & professional website, but also cool and interesting how they carry through some of their branding and toony graphic elements. We like the use of big circles to highlight certain elements. We feel that this would play well for us too because we already use some of these big circles/bubbles in our bokeh background.

2) www.velquinpixel.example = these guys have the same kind of top to bottom layout with big chunks for each section. They come across as a little more "buttoned up" then craftwombats, but still friendly enough to make a small business owner feel comfortable.

There are a few elements that we consider part of our brand and that we want to continue to use in our new design. They are as follows:
1) The nerdy scientist dude....we have 50+ variations of this little guy in every file format you need. I'll try to upload the whole set....at the least, you'll have one or two examples.

2) The electric green bokeh background you see at the top of each page of our website.

3) And our logo of course which is included in uploads.

Please feel free to ask me any questions. We're really open to new and fresh ideas and creativity. So...let 'r rip!

```html
<!DOCTYPE html>
<html lang="en">
<head>
<meta charset="utf-8">
<title>PebbleCraft Hub – Digital Marketing</title>
<link href="https://fonts.googleapis.com/css2?family=Open+Sans:wght@300;400;600;700;800&display=swap" rel="stylesheet">
<style>
:root{
  --green:#4aa51c;
  --green-dark:#2f8a0c;
  --green-light:#9fd83f;
  --orange:#f5891f;
  --orange-dark:#e06e0c;
  --text:#444;
  --muted:#888;
  --line:#dcdcdc;
  --band:#f1f1f1;
  --footer:#222;
}
*{box-sizing:border-box;margin:0;padding:0}
html,body{width:1200px;height:4044px;overflow:hidden}
body{font-family:"Open Sans",Arial,sans-serif;color:var(--text);background:#fff;position:relative}
.section{position:absolute;left:0;width:1200px}
.wrap{position:relative;width:976px;margin:0 auto;height:100%}

/* header */
.site-header{top:0;height:132px}
.brand{position:absolute;left:0;top:34px;display:flex;align-items:center;gap:12px}
.brand-dot{width:40px;height:40px;border-radius:50%;background:var(--green)}
.brand-name{font-size:30px;font-weight:800;color:var(--green);line-height:1}
.phone{position:absolute;right:0;top:46px;display:flex;align-items:center;gap:10px;font-size:24px;font-weight:600;color:#333}
.phone svg{width:26px;height:26px}

/* nav */
.main-nav{top:132px;height:44px;background:linear-gradient(#f9a23b,var(--orange-dark))}
.main-nav ul{list-style:none;display:flex;gap:34px;height:44px;align-items:center}
.main-nav li{font-size:13px;color:#fff;font-weight:600}
.main-nav li.active{background:#fff;color:var(--orange-dark);padding:4px 10px;border-radius:2px}
.search{position:absolute;right:0;top:9px;width:270px;height:26px;background:#fff;border-radius:2px;font-size:12px;color:#aaa;padding:5px 10px}
.search svg{position:absolute;right:8px;top:6px;width:14px;height:14px}

/* hero */
.hero{top:176px;height:424px;background:radial-gradient(circle at 78% 40%,var(--green-light),var(--green) 45%,var(--green-dark));overflow:hidden}
.notch{position:absolute;left:560px;width:80px;height:22px}
.hero .notch{top:0}
.hero-text{position:absolute;left:0;top:58px;color:#fff}
.hero-text .pre{font-size:40px;font-weight:300;line-height:1.1}
.hero-text h1{font-size:48px;font-weight:700;line-height:1.1;margin-bottom:22px}
.hero-text p{font-size:18px;font-weight:700;line-height:1.35}
.btn{display:inline-flex;align-items:center;gap:10px;border-radius:22px;color:#fff;font-weight:700}
.btn-orange{background:var(--orange);font-size:15px;padding:10px 12px 10px 22px;margin-top:36px}
.btn-arrow{width:24px;height:24px;border-radius:50%;background:#fff;display:flex;align-items:center;justify-content:center}
.btn-arrow svg{width:12px;height:12px}
.mascot{position:absolute;left:690px;top:20px;width:260px;height:330px;border-radius:130px 130px 20px 20px;background:linear-gradient(#e9f5d8,#b9dd8b);opacity:.85}
.engine-badges{position:absolute;left:570px;top:350px;display:flex;gap:14px}
.engine-badges span{width:100px;height:44px;background:#fff;border-radius:3px;box-shadow:0 2px 4px rgba(0,0,0,.2)}

/* services */
.services{top:720px;height:280px}
.service-row{display:flex;justify-content:space-between;padding:0 30px}
.service{width:260px;text-align:center}
.service-icon{width:70px;height:70px;border-radius:50%;background:var(--orange);margin:0 auto 14px;display:flex;align-items:center;justify-content:center}
.service-icon svg{width:34px;height:34px}
.service h3{font-size:18px;font-weight:700;color:#333;line-height:1.25;margin-bottom:8px}
.service p{font-size:12.5px;color:var(--muted);line-height:1.5}

/* what we do */
.what-we-do{top:1048px;height:360px;background:var(--band)}
.devices{position:absolute;left:40px;top:50px;width:410px;height:260px;background:linear-gradient(135deg,#3a3a3a,#6fbf2c 60%,#2b2b2b);border-radius:6px}
.what-text{position:absolute;left:520px;top:40px;width:450px}
.what-text h2{font-size:36px;font-weight:700;color:var(--green);margin-bottom:8px}
.what-text .lead{font-size:13px;color:#555;margin-bottom:8px}
.what-text .lead b{display:block;font-size:12px;color:#333}
.what-text p{font-size:12.5px;color:var(--muted);line-height:1.55}
.btn-green{background:var(--green);font-size:12px;padding:6px 8px 6px 16px;margin-top:18px}
.btn-green .btn-arrow{width:18px;height:18px}

/* team */
.team{top:1460px;height:500px;text-align:center}
.section-title{font-size:30px;font-weight:700;color:#333}
.section-sub{font-size:13px;color:var(--muted);margin-top:4px}
.team-row{display:flex;justify-content:space-between;padding:0 40px;margin-top:46px}
.member{width:200px}
.portrait{width:150px;height:150px;border-radius:50%;margin:0 auto 16px;background:linear-gradient(#eaeaea,#bdbdbd);border:4px solid #eee}
.member h4{font-size:18px;font-weight:700;color:#333;margin-bottom:4px}
.member p{font-size:12px;color:var(--muted);line-height:1.5}

/* portfolio */
.portfolio{top:1968px;height:472px;background:radial-gradient(circle at 30% 40%,var(--green-light),var(--green) 50%,var(--green-dark))}
.portfolio .notch.top{top:0}
.portfolio .notch.bottom{bottom:0}
.work-grid{display:grid;grid-template-columns:repeat(4,214px);gap:22px 20px;justify-content:center;padding-top:50px}
.work{height:170px;border:4px solid #fff;box-shadow:0 3px 8px rgba(0,0,0,.3)}
.work:nth-child(odd){background:linear-gradient(#2d5d9e,#dfe7f1)}
.work:nth-child(even){background:linear-gradient(#8b3c2a,#f0e6d6)}

/* why choose */
.why{top:2480px;height:620px}
.why h2{position:absolute;left:0;top:100px;font-size:30px;font-weight:700;color:var(--green)}
.why .intro{position:absolute;left:0;top:150px;width:520px;font-size:12.5px;color:var(--muted);line-height:1.5}
.checklist{position:absolute;left:0;top:230px;list-style:none;width:560px}
.checklist li{display:flex;align-items:center;gap:12px;font-size:13px;color:#555;height:34px;border-bottom:1px solid #eee}
.box{width:18px;height:18px;border:1px solid #aaa;background:#fff;display:flex;align-items:center;justify-content:center}
.box svg{width:14px;height:14px}
.monitor{position:absolute;left:620px;top:80px;width:356px;height:400px;border-radius:8px;background:linear-gradient(#1f1f1f,#3c3c3c 80%,#cfcfcf)}

/* support */
.support{top:3120px;height:320px;background:radial-gradient(circle at 60% 40%,var(--green-light),var(--green) 55%,var(--green-dark))}
.support .notch{top:0}
.support-row{display:flex;justify-content:center;gap:56px;padding-top:100px}
.support-card{width:250px;height:170px;background:#fff;border-radius:3px;text-align:center;padding:44px 18px 0;position:relative;box-shadow:0 3px 8px rgba(0,0,0,.25)}
.support-card .badge{position:absolute;left:97px;top:-28px;width:56px;height:56px;border-radius:50%;background:var(--orange);border:4px solid #fff}
.support-card h4{font-size:17px;font-weight:700;color:#333;margin-bottom:8px}
.support-card p{font-size:12px;color:var(--muted);line-height:1.5}

/* contact */
.contact{top:3480px;height:520px;text-align:center}
.contact-form{width:620px;margin:36px auto 0;text-align:left}
.field{height:38px;border:1px solid var(--line);border-radius:3px;font-size:12px;color:#aaa;padding:11px 12px;margin-bottom:10px}
.field.area{height:108px}
.submit-row{text-align:center}
.btn-submit{background:var(--green);font-size:15px;padding:8px 10px 8px 26px;margin-top:8px}

/* footer */
.site-footer{top:3996px;height:48px;background:var(--footer);color:#aaa;font-size:12px;text-align:center;line-height:48px}
</style>
</head>
<body>

<header class="section site-header">
  <div class="wrap">
    <div class="brand"><span class="brand-dot"></span><span class="brand-name">PebbleCraft Hub</span></div>
    <div class="phone">
      <svg viewBox="0 0 24 24"><path fill="#f5891f" d="M6.6 10.8a15.1 15.1 0 0 0 6.6 6.6l2.2-2.2c.3-.3.7-.4 1-.2 1.1.4 2.3.6 3.6.6.6 0 1 .4 1 1V20c0 .6-.4 1-1 1A17 17 0 0 1 3 4c0-.6.4-1 1-1h3.5c.6 0 1 .4 1 1 0 1.3.2 2.5.6 3.6.1.3 0 .7-.2 1z"/></svg>
      (800) 555-0142
    </div>
  </div>
</header>

<nav class="section main-nav">
  <div class="wrap">
    <ul>
      <li class="active">HOME</li><li>Who we are</li><li>What we do</li><li>How it works</li><li>Why choose us</li><li>Get in touch</li>
    </ul>
    <div class="search">Search
      <svg viewBox="0 0 16 16"><circle cx="6.5" cy="6.5" r="4.5" fill="none" stroke="#999" stroke-width="2"/><path d="M10 10l4 4" stroke="#999" stroke-width="2"/></svg>
    </div>
  </div>
</nav>

<section class="section hero">
  <svg class="notch" viewBox="0 0 80 22"><path d="M0 0h80L40 22z" fill="#fff"/></svg>
  <div class="wrap">
    <div class="hero-text">
      <div class="pre">We Create</div>
      <h1>Marketing Chemistry</h1>
      <p>Website Leads Banging on Your Door?<br>It's Not Your Fault... We Can Help!</p>
      <span class="btn btn-orange">Free Website Analysis
        <span class="btn-arrow"><svg viewBox="0 0 12 12"><path d="M4 2l4 4-4 4" fill="none" stroke="#f5891f" stroke-width="2"/></svg></span>
      </span>
    </div>
    <div class="mascot" role="img" aria-label="Mascot character holding a laptop"></div>
    <div class="engine-badges"><span></span><span></span><span></span></div>
  </div>
</section>

<section class="section services">
  <div class="wrap">
    <div class="service-row">
      <div class="service">
        <div class="service-icon"><svg viewBox="0 0 24 24"><rect x="3" y="4" width="18" height="13" rx="1" fill="none" stroke="#fff" stroke-width="2"/><path d="M8 21h8M12 17v4" stroke="#fff" stroke-width="2"/></svg></div>
        <h3>Web Design &amp;<br>Development</h3>
        <p>Clean, fast websites built to turn visitors into leads and keep your brand looking sharp.</p>
      </div>
      <div class="service">
        <div class="service-icon"><svg viewBox="0 0 24 24"><path d="M12 2a7 7 0 0 0-7 7c0 5 7 13 7 13s7-8 7-13a7 7 0 0 0-7-7z" fill="none" stroke="#fff" stroke-width="2"/><circle cx="12" cy="9" r="2.5" fill="#fff"/></svg></div>
        <h3>Local Search<br>Marketing</h3>
        <p>Get found by nearby customers with listings and local pages that rank where it counts.</p>
      </div>
      <div class="service">
        <div class="service-icon"><svg viewBox="0 0 24 24"><circle cx="10" cy="10" r="6" fill="none" stroke="#fff" stroke-width="2.4"/><path d="M15 15l6 6" stroke="#fff" stroke-width="2.6"/></svg></div>
        <h3>Search Engine<br>Optimization</h3>
        <p>Smart keyword and content work that lifts your rankings and brings steady traffic.</p>
      </div>
    </div>
  </div>
</section>

<section class="section what-we-do">
  <div class="wrap">
    <div class="devices" role="img" aria-label="Website shown on a phone, tablet and laptop"></div>
    <div class="what-text">
      <h2>What We Do.</h2>
      <div class="lead">In a nutshell, we design websites that pop and develop marketing campaigns that work!
        <b>How do we do it? Thank you for asking.</b></div>
      <p>First off, we get your website into top shape. If you don't have one, no problem, we can build you a fresh site loaded with features that help you rank in your area. Once it's live, focused marketing messages bring new visitors to you, ready to reach out by filling out your contact form or picking up the phone today.</p>
      <span class="btn btn-green">Read More
        <span class="btn-arrow"><svg viewBox="0 0 12 12"><path d="M4 2l4 4-4 4" fill="none" stroke="#4aa51c" stroke-width="2"/></svg></span>
      </span>
    </div>
  </div>
</section>

<section class="section team">
  <div class="wrap">
    <h2 class="section-title">Meet Our Team</h2>
    <p class="section-sub">The friendly people behind every project we ship.</p>
    <div class="team-row">
      <div class="member"><div class="portrait" role="img" aria-label="Portrait of John Doe"></div><h4>John Doe</h4><p>Strategy lead who keeps every campaign on track and on budget.</p></div>
      <div class="member"><div class="portrait" role="img" aria-label="Portrait of Lucy"></div><h4>Lucy</h4><p>Designer who turns rough ideas into clean, friendly layouts.</p></div>
      <div class="member"><div class="portrait" role="img" aria-label="Portrait of James"></div><h4>James</h4><p>Developer who builds fast sites and fixes things quickly.</p></div>
      <div class="member"><div class="portrait" role="img" aria-label="Portrait of Emily"></div><h4>Emily</h4><p>Search specialist who helps clients climb the rankings.</p></div>
    </div>
  </div>
</section>

<section class="section portfolio">
  <svg class="notch top" viewBox="0 0 80 22"><path d="M0 0h80L40 22z" fill="#fff"/></svg>
  <div class="work-grid">
    <div class="work" role="img" aria-label="Client website screenshot"></div>
    <div class="work" role="img" aria-label="Client website screenshot"></div>
    <div class="work" role="img" aria-label="Client website screenshot"></div>
    <div class="work" role="img" aria-label="Client website screenshot"></div>
    <div class="work" role="img" aria-label="Client website screenshot"></div>
    <div class="work" role="img" aria-label="Client website screenshot"></div>
    <div class="work" role="img" aria-label="Client website screenshot"></div>
    <div class="work" role="img" aria-label="Client website screenshot"></div>
  </div>
  <svg class="notch bottom" viewBox="0 0 80 22"><path d="M0 22h80L40 0z" fill="#fff"/></svg>
</section>

<section class="section why">
  <div class="wrap">
    <h2>Why Would You Choose Anyone Else?</h2>
    <p class="intro">Here at PebbleCraft Hub, our team of creative designers and clever marketers works hard every day to give you quality results and friendly service.</p>
    <ul class="checklist">
      <li><span class="box"><svg viewBox="0 0 14 14"><path d="M2 7l3 3 7-7" fill="none" stroke="#4aa51c" stroke-width="2.4"/></svg></span>Honest pricing with clear monthly reports you can actually read</li>
      <li><span class="box"></span>Local experts who answer the phone</li>
      <li><span class="box"></span>Proven results for small businesses</li>
      <li><span class="box"></span>Websites built for every screen size</li>
      <li><span class="box"></span>No long contracts or hidden fees</li>
    </ul>
    <div class="monitor" role="img" aria-label="Desktop monitor with the mascot character beside it"></div>
  </div>
</section>

<section class="section support">
  <svg class="notch" viewBox="0 0 80 22"><path d="M0 0h80L40 22z" fill="#fff"/></svg>
  <div class="support-row">
    <div class="support-card"><span class="badge"></span><h4>FriendLoop Support</h4><p>We set up and manage your page so fans can find you and stay in touch.</p></div>
    <div class="support-card"><span class="badge"></span><h4>Chirper Support</h4><p>Timely posts and replies that keep your brand part of the conversation.</p></div>
    <div class="support-card"><span class="badge"></span><h4>CirclePlus Support</h4><p>Profiles tuned to boost your local search presence and reviews.</p></div>
  </div>
</section>

<section class="section contact">
  <h2 class="section-title">Ask An Expert</h2>
  <p class="section-sub">You can get in touch with us any time you want!</p>
  <div class="contact-form">
    <div class="field">Your Name</div>
    <div class="field">Your Email Address</div>
    <div class="field">Your Telephone Number</div>
    <div class="field">Your Web Address</div>
    <div class="field area">What would you like to ask?</div>
    <div class="submit-row"><span class="btn btn-submit">Submit
      <span class="btn-arrow"><svg viewBox="0 0 12 12"><path d="M4 2l4 4-4 4" fill="none" stroke="#4aa51c" stroke-width="2"/></svg></span></span></div>
  </div>
</section>

<footer class="section site-footer">Copyright © 2014. PebbleCraftHub.com All Rights Reserved</footer>

</body>
</html>
```